KORBALT

The business want a professional looking business card. We have a scetch we will add but want the extra upgrade, and would like more suggestions for variations of our business cards.

```html
<!DOCTYPE html>
<html lang="en">
<head>
<meta charset="utf-8">
<title>KORBALT Business Card</title>
<link rel="stylesheet" href="https://fonts.googleapis.com/css2?family=Montserrat:wght@400;500;600&display=swap">
<style>
  :root {
    --canvas: #ffffff;
    --card-light: #fdfdfc;
    --card-light-tone: #f1f1ef;
    --card-dark: #121212;
    --card-dark-tone: #1c1c1c;
    --gold: #9c7c33;
    --gold-bright: #d9b25e;
    --shadow: rgba(0, 0, 0, 0.22);
  }
  * { margin: 0; padding: 0; box-sizing: border-box; }
  html, body {
    width: 1200px;
    height: 1200px;
    overflow: hidden;
    background: var(--canvas);
  }
  .canvas {
    position: relative;
    width: 1200px;
    height: 1200px;
    font-family: "Montserrat", Arial, sans-serif;
  }
  .card {
    position: absolute;
    top: 425px;
    width: 540px;
    height: 350px;
    box-shadow: 0 10px 34px var(--shadow);
    overflow: hidden;
  }
  .card-front { left: 40px; }
  .card-back { left: 620px; }

  .card-texture {
    position: absolute;
    inset: 0;
  }
  .card-front .card-texture {
    background: radial-gradient(circle at 50% 50%, var(--card-light) 0%, var(--card-light-tone) 100%);
  }
  .card-back .card-texture {
    background: radial-gradient(circle at 50% 50%, var(--card-dark-tone) 0%, var(--card-dark) 100%);
  }

  .front-brand {
    position: absolute;
    top: 52px;
    right: 34px;
    width: 130px;
    text-align: center;
    font-weight: 600;
    font-size: 15px;
    letter-spacing: 0.22em;
    color: var(--gold);
  }

  .identity {
    position: absolute;
    top: 176px;
    left: 0;
    right: 0;
    text-align: center;
    color: var(--gold);
  }
  .identity-name {
    font-weight: 500;
    font-size: 17px;
    letter-spacing: 0.16em;
  }
  .identity-position {
    margin-top: 9px;
    font-weight: 500;
    font-size: 12px;
    letter-spacing: 0.14em;
  }
  .identity-role {
    margin-top: 5px;
    font-size: 8px;
    letter-spacing: 0.12em;
  }

  .contact {
    position: absolute;
    bottom: 26px;
    font-size: 10px;
    line-height: 1.35;
    color: var(--gold);
  }
  .contact-reach { left: 34px; }
  .contact-address { right: 34px; text-align: right; }

  .back-brand {
    position: absolute;
    inset: 0;
    display: flex;
    align-items: center;
    justify-content: center;
    gap: 18px;
  }
  .back-brand-dot {
    width: 18px;
    height: 18px;
    border-radius: 50%;
    background: var(--gold-bright);
  }
  .back-brand-name {
    font-weight: 600;
    font-size: 40px;
    letter-spacing: 0.2em;
    color: var(--gold-bright);
  }
</style>
</head>
<body>
<main class="canvas">
  <section class="card card-front">
    <div class="card-texture" role="img" aria-label="Faint light grey repeating leaf-petal pattern across the white card"></div>
    <div class="front-brand">KORBALT</div>
    <div class="identity">
      <p class="identity-name">NAME AND LAST NAME</p>
      <p class="identity-position">POSITION, LEED</p>
      <p class="identity-role">CEO/PRINCIPAL</p>
    </div>
    <div class="contact contact-reach">
      <p>(111) 111-1111</p>
      <p>name.lastname@companywebsite.com</p>
      <p>companywebsite.com</p>
    </div>
    <div class="contact contact-address">
      <p>1111 address address</p>
      <p>address placeholder</p>
      <p>111111 postal code</p>
    </div>
  </section>

  <section class="card card-back">
    <div class="card-texture" role="img" aria-label="Subtle dark tone-on-tone repeating leaf-petal pattern across the black card"></div>
    <div class="back-brand">
      <span class="back-brand-dot"></span>
      <span class="back-brand-name">KORBALT</span>
    </div>
  </section>
</main>
</body>
</html>
```